Stationery Design Project

Please use logo on top corner and place a watermark of the logo on center of the page. Also please add address on bottom as a watermark type of font/colour.

Target Market(s)

FInancial profesionals and high net work individuals

Font styles to use
Serif
Sans Serif

```html
<!DOCTYPE html>
<html lang="en">
<head>
<meta charset="utf-8">
<title>Marlow Equity Finance – Business Card</title>
<link href="https://fonts.googleapis.com/css2?family=Cinzel:wght@400&family=Arimo:wght@400;700&display=swap" rel="stylesheet">
<style>
  :root {
    --page: #ffffff;
    --card: #222222;
    --brand-blue: #4a67ab;
    --label-blue: #5b7cc9;
    --white: #ffffff;
  }
  * { margin: 0; padding: 0; box-sizing: border-box; }
  html, body { width: 998px; height: 1200px; overflow: hidden; background: var(--page); }
  .canvas { position: relative; width: 998px; height: 1200px; font-family: "Arimo", Arial, sans-serif; color: var(--white); }
  .card { position: absolute; left: 36px; width: 926px; background: var(--card); overflow: hidden; }
  .card--front { top: 43px; height: 543px; }
  .card--back { top: 614px; height: 543px; }
  .card svg.shapes { position: absolute; inset: 0; }

  .wordmark { position: absolute; font-family: "Cinzel", "Times New Roman", serif; font-weight: 400; color: var(--brand-blue); line-height: 1; white-space: nowrap; }
  .wordmark__name { display: block; }
  .wordmark__sub { display: block; }
  .card--front .wordmark { left: 0; width: 926px; top: 310px; text-align: center; }
  .card--front .wordmark__name { font-size: 66px; letter-spacing: 1px; }
  .card--front .wordmark__sub { font-size: 25px; margin-top: 12px; letter-spacing: 1px; }
  .card--back .wordmark { left: 222px; top: 632px; top: 28px; }
  .card--back .wordmark__name { font-size: 64px; letter-spacing: 1px; }
  .card--back .wordmark__sub { font-size: 25px; margin-top: 8px; margin-left: 36px; letter-spacing: 1px; }

  .holder { position: absolute; transform: rotate(-90deg); transform-origin: center; text-align: center; white-space: nowrap; width: 320px; }
  .holder__name { left: -56px; top: 306px; font-size: 34px; font-weight: 700; }
  .holder__title { left: -11px; top: 314px; font-size: 17px; }

  .address { position: absolute; left: 400px; width: 324px; top: 222px; text-align: center; font-size: 19px; line-height: 24px; }
  .contact { position: absolute; font-size: 19px; line-height: 24px; text-align: center; }
  .contact--phones { left: 200px; width: 320px; top: 372px; }
  .contact--web { left: 614px; width: 320px; top: 372px; text-align: center; transform: translateX(-40px); }
  .contact .label { color: var(--label-blue); }
  .tagline { position: absolute; left: 140px; width: 854px; top: 502px; text-align: center; font-size: 20px; font-weight: 700; letter-spacing: 6px; }
</style>
</head>
<body>
<main class="canvas">

  <section class="card card--front" aria-label="Card front">
    <svg class="shapes" width="926" height="543" viewBox="0 0 926 543" aria-hidden="true">
      <rect class="band" x="0" y="172" width="926" height="113" fill="var(--brand-blue)"/>
      <circle class="band-seal" cx="457" cy="227" r="112" fill="var(--card)"/>
    </svg>
    <div class="wordmark">
      <span class="wordmark__name">MARLOW</span>
      <span class="wordmark__sub">EQUITY FINANCE</span>
    </div>
  </section>

  <section class="card card--back" aria-label="Card back">
    <svg class="shapes" width="926" height="543" viewBox="0 0 926 543" aria-hidden="true">
      <rect class="side-band" x="65" y="0" width="126" height="543" fill="var(--brand-blue)"/>
      <path class="side-panel" d="M65 185 Q128 150 191 185 L191 473 Q128 508 65 473 Z" fill="var(--card)"/>
      <line class="timeline" x1="277" y1="322" x2="849" y2="322" stroke="var(--brand-blue)" stroke-width="3"/>
      <g class="ticks" stroke="var(--brand-blue)" stroke-width="3">
        <line x1="357" y1="336" x2="357" y2="356"/>
        <line x1="562" y1="288" x2="562" y2="308"/>
        <line x1="772" y1="336" x2="772" y2="356"/>
      </g>
      <g class="nodes" fill="var(--brand-blue)">
        <circle cx="357" cy="322" r="24"/>
        <circle cx="562" cy="322" r="24"/>
        <circle cx="772" cy="322" r="24"/>
      </g>
      <g class="icon-phone" fill="var(--white)">
        <path d="M344 316 q13 -9 26 0 l0 4 l-6 0 l0 -3 q-7 -2 -14 0 l0 3 l-6 0 z"/>
        <path d="M349 321 h16 l3 12 h-22 z"/>
      </g>
      <g class="icon-home" fill="var(--white)">
        <path d="M562 308 l14 13 h-4 v12 h-7 v-7 h-6 v7 h-7 v-12 h-4 z"/>
      </g>
      <g class="icon-globe" fill="none" stroke="var(--white)" stroke-width="1.8">
        <circle cx="772" cy="322" r="12"/>
        <ellipse cx="772" cy="322" rx="5" ry="12"/>
        <line x1="760" y1="322" x2="784" y2="322"/>
        <line x1="762" y1="315" x2="782" y2="315"/>
        <line x1="762" y1="329" x2="782" y2="329"/>
      </g>
    </svg>

    <div class="wordmark">
      <span class="wordmark__name">MARLOW</span>
      <span class="wordmark__sub">EQUITY FINANCE</span>
    </div>

    <div class="holder holder__name">Daniel Reyes</div>
    <div class="holder holder__title">CEO / Senior Network Engineer</div>

    <p class="address">1234 Street, Suite A<br>New York, USA 12345</p>

    <p class="contact contact--phones">
      123.456.7890 <span class="label">Help Desk</span><br>
      123.456.7890 <span class="label">Direct</span><br>
      123.456.7890 <span class="label">Cell</span>
    </p>
    <p class="contact contact--web">
      information@marlowequity.com<br>
      www.marlowequity.com
    </p>

    <p class="tagline">Marlow Equity Finance</p>
  </section>

</main>
</body>
</html>
```